A Lantern on the pier.

I need a book cover (and back cover) design for a novel. The novel is a thiller. ´Synopsis: During the party after an awards ceremony at prestigious institution, one of the young awarders dissapear. The last place where he left a trace was close to a giant chessboard in the grass of the beautiful gardens of the place of ceremony. The detective in charge of finding the missing person and find out what happened will gradually discover that the institution is not all that it seems.
The book cover size will be 9" x 6" and the title of the novel "A lantern on the pier" will be name in spanish "Una linterna en el muelle". The back cover will have a synopsis (in spanish )that i will develop later on.
One suggestion for the design: I always love the art of MILO TRENT for movie posters, so I´m looking for something of similar style, you know (the girl who sold paper kites, North pier ballad, halvorn, ledger of shadows, etc

```html
<!DOCTYPE html>
<html lang="en">
<head>
<meta charset="utf-8">
<title>A Lantern on the Pier — Book Cover</title>
<link rel="stylesheet" href="https://fonts.googleapis.com/css2?family=Londrina+Solid:wght@300;400;900&display=swap">
<style>
  :root {
    --red-deep: #2e0906;
    --red-mid: #5e140e;
    --red-bright: #8e2218;
    --ink-white: #ffffff;
    --ink-yellow: #f2c300;
    --ink-grey: #c9c9c9;
    --title-font: "Londrina Solid", "Arial Narrow", sans-serif;
  }
  * { margin: 0; padding: 0; box-sizing: border-box; }
  html, body {
    width: 800px;
    height: 1200px;
    overflow: hidden;
    background: var(--red-deep);
  }
  .cover {
    position: relative;
    width: 800px;
    height: 1200px;
    overflow: hidden;
    background: var(--red-deep);
  }
  .cover-artwork {
    position: absolute;
    inset: 0;
    background:
      radial-gradient(ellipse 62% 55% at 50% 48%, var(--red-bright) 0%, var(--red-mid) 55%, var(--red-deep) 100%);
  }
  .title {
    position: absolute;
    left: 0;
    right: 0;
    top: 0;
    font-family: var(--title-font);
    text-transform: uppercase;
    text-align: center;
    color: var(--ink-white);
  }
  .title-line {
    position: absolute;
    left: 0;
    right: 0;
    display: block;
    line-height: 1;
    font-weight: 900;
  }
  .title-article {
    top: 128px;
    font-size: 232px;
  }
  .title-main {
    top: 340px;
    font-size: 222px;
    letter-spacing: -4px;
  }
  .title-joiner {
    top: 556px;
    font-size: 204px;
    letter-spacing: 6px;
  }
  .title-place {
    top: 752px;
    font-size: 236px;
    letter-spacing: 18px;
    color: var(--ink-yellow);
  }
  .author {
    position: absolute;
    left: 0;
    right: 0;
    top: 1088px;
    text-align: center;
    font-family: var(--title-font);
    font-weight: 300;
    font-size: 50px;
    line-height: 1;
    letter-spacing: 2px;
    color: var(--ink-grey);
    word-spacing: 14px;
  }
</style>
</head>
<body>
  <main class="cover">
    <div class="cover-artwork" role="img"
         aria-label="Dark red checkerboard lawn seen from above, edged with shadowy garden foliage, with black climbing vines, leaves and scattered white chess pieces around the title"></div>

    <h1 class="title">
      <span class="title-line title-article">A</span>
      <span class="title-line title-main">Lantern</span>
      <span class="title-line title-joiner">On the</span>
      <span class="title-line title-place">Pier</span>
    </h1>

    <p class="author">MILO TRENT</p>
  </main>
</body>
</html>
```